Your Health, Your Time, Your Way: Personalized, Concierge Care Elevated to Modern Medicine

We need to incorporate an image of our new doctor (Dr. Malvina Okoruwe, MD) with our office logo ( Harborline Family Clinic) and dialogue that shows how simple it is to schedule a free consult and learn what our office has to offer patients. The colors should be consistent with our website- the CMYK codes will be attached for your use below. The font should be easy to read. The text should be clear, and convey value to the patient for chosing us over anyone else ( we offer primary care, preventive medicine, urgen care and functional medicine with 24 hour direct access to care with some of our strengths including focus on individualized care, cutting edge medicine, blended functional and traditional style. We aim to transform lives through patient centered innovative and individualized care plan. I have attached a "mock" image but the details ( office address, name, phone number are incorrect) The correct info is Harborline Family Clinic 4187 Wrenfield Ave Suite 214, Clearwater, FL 33759 and phone number (727)482-3095. A possible hook could read: welcoming new patients now- Your Health, Your Time, Your Way: Personalized Care Meets Modern Medicine
Updates

I did not realize that there was a tab with more information to fill for the designers to see, or for me to upload the basic information they need to create the design.

Target Market(s)

Patients over 18 years of age with interest in longevity, functional and traditional medicine; the postcards will be mailed to our CURRENT patients, and they are a reminder of what we do, new patient availability AND a request for them to refer friends or families

Industry/Entity Type

medical

Font styles to use
Sans Serif

Colors

Designer to choose colors to be used in the design.

Requirements
Must have
• simple reminder to current patients of what we offer, and a call to action for our patients to refer friends and family for same level of excellence;consistency with brand ( see business card and cmyx codes for colors);photo of new physician; logo Harborline Family Clinic, web site (https://harborlinefamilyclinic.net); Must clearly express accepting new patients; simple to call/email to schedule free consultation;; include our email (office@harborlinefamilyclinic.org), phone number (727)482-3095; our address 4187 Wrenfield Ave Suite 214, Clearwater, FL 33759
Nice to have
• photo of our new physician ( in blue jacket: Dr. Malvina Okoruwe, MD) should not take up too much space
Should not have
• clutter, or close text; full sentences( bulleted text preferred)

```html
<!DOCTYPE html>
<html lang="en">
<head>
<meta charset="utf-8">
<title>Harborline Family Clinic – Referral Postcard</title>
<link href="https://fonts.googleapis.com/css2?family=Lato:wght@400;700;900&family=Arimo:wght@400&display=swap" rel="stylesheet">
<style>
  :root {
    --board: #939393;
    --slate: #5d6a7c;
    --slate-dark: #4b5667;
    --slate-soft: #7a8596;
    --ink: #4f5b6b;
    --forest: #1f3d2a;
    --white: #ffffff;
  }
  * { margin: 0; padding: 0; box-sizing: border-box; }
  html, body { width: 1072px; height: 1200px; overflow: hidden; }
  body {
    background: var(--board);
    font-family: "Lato", sans-serif;
    position: relative;
  }
  .postcard {
    position: absolute;
    left: 230px;
    width: 607px;
    height: 423px;
    overflow: hidden;
    background: var(--white);
    box-shadow: 0 3px 8px rgba(0,0,0,.35);
  }
  .postcard--front { top: 127px; }
  .postcard--back { top: 628px; background: var(--slate); }
  .postcard svg.shapes { position: absolute; inset: 0; }
  .abs { position: absolute; }
  .side-label {
    position: absolute; left: 0; width: 1072px; text-align: center;
    color: var(--white); font-weight: 900; font-size: 21px; letter-spacing: 4.5px;
  }

  /* brand name block */
  .brand { display: flex; align-items: center; gap: 7px; color: var(--slate); }
  .brand__dot { width: 22px; height: 22px; border-radius: 50%; background: var(--slate); flex: none; }
  .brand__name { font-size: 15px; font-weight: 700; line-height: 1.1; }

  /* front */
  .headline {
    left: 260px; width: 308px; top: 50px; text-align: center;
    color: var(--white); font-weight: 900; font-size: 37px; line-height: 35px;
  }
  .headline span { display: block; white-space: nowrap; }
  .headline .second { font-size: 34px; }
  .tagline-pill {
    left: 260px; top: 121px; width: 308px; height: 21px;
    background: var(--white); border-radius: 11px;
    box-shadow: 0 2px 0 var(--slate-dark);
    color: var(--slate); font-weight: 700; font-size: 12.5px; letter-spacing: 2px;
    display: flex; align-items: center; justify-content: center;
  }
  .subline {
    left: 240px; width: 348px; top: 146px; text-align: center;
    color: var(--white); font-weight: 700; font-size: 10.4px;
  }
  .doctor-name { left: 28px; top: 177px; color: var(--ink); font-weight: 900; font-size: 11.6px; }
  .doctor-bio { left: 29px; top: 194px; color: var(--ink); font-size: 9.2px; line-height: 11.3px; }

  .cta-kicker { left: 29px; top: 284px; font-weight: 900; font-size: 12.2px; letter-spacing: .7px; color: var(--ink); }
  .cta-main { left: 28px; top: 297px; font-weight: 900; font-size: 20px; letter-spacing: .8px; color: var(--ink); }
  .postcard--back .cta-kicker, .postcard--back .cta-main { color: var(--white); }

  .phone-pill {
    left: 25px; top: 325px; width: 219px; height: 34px; border-radius: 17px;
    display: flex; align-items: center; gap: 8px; padding-left: 5px;
    font-weight: 900; font-size: 22.5px; letter-spacing: .6px;
  }
  .phone-pill--slate { background: var(--slate); border: 2px solid var(--slate-dark); color: var(--white); }
  .phone-pill--white { background: var(--white); color: var(--slate); top: 326px; height: 30px; left: 28px; width: 214px; }
  .phone-pill__icon { width: 24px; height: 24px; border-radius: 50%; flex: none; display: flex; align-items: center; justify-content: center; }
  .phone-pill--slate .phone-pill__icon { background: var(--white); }
  .phone-pill--white .phone-pill__icon { background: var(--slate); width: 22px; height: 22px; }

  .contact-line { left: 28px; display: flex; align-items: center; gap: 8px; font-size: 12.6px; color: var(--ink); }
  .postcard--back .contact-line { color: var(--white); }
  .contact-line svg { width: 11px; height: 11px; flex: none; }

  /* back */
  .welcome { left: 29px; top: 187px; color: var(--white); font-weight: 900; font-size: 16.2px; line-height: 18.5px; }
  .welcome-copy { left: 29px; top: 228px; color: var(--white); font-size: 7.9px; line-height: 10.1px; width: 175px; }
  .return-address { right: 111px; top: 32px; text-align: right; color: #222; font-size: 12.4px; line-height: 17px; }
  .return-address strong { font-weight: 900; }
  .indicia {
    left: 514px; top: 30px; width: 67px; height: 67px; border: 1px solid #222;
    font-family: "Arimo", sans-serif; font-size: 8.2px; line-height: 10.3px; color: #222;
    text-align: center; padding-top: 5px;
  }
  .benefits-title { right: 27px; top: 130px; text-align: right; color: var(--forest); font-weight: 900; font-size: 12.6px; line-height: 15px; }
  .benefits-list { right: 26px; top: 165px; list-style: none; text-align: right; }
  .benefits-list li {
    display: flex; justify-content: flex-end; align-items: center; gap: 5px;
    font-size: 8.5px; line-height: 12.25px; color: var(--forest);
  }
  .benefits-list li::after {
    content: "✓"; width: 7.5px; height: 7.5px; border-radius: 50%;
    background: var(--forest); color: var(--white); font-size: 5.5px; line-height: 7.5px;
    text-align: center; font-weight: 900;
  }
  .mail-block {
    left: 450px; top: 317px; width: 131px; height: 38px; border: 1px solid #222;
    font-family: "Arimo", sans-serif; font-size: 8.6px; line-height: 10.5px; color: #222;
    padding: 6px 0 0 5px;
  }
</style>
</head>
<body>

<!-- FRONT -->
<section class="postcard postcard--front">
  <svg class="shapes" viewBox="0 0 607 423" width="607" height="423" aria-hidden="true">
    <defs>
      <radialGradient id="frontGlow" cx="0.7" cy="0.25" r="0.7">
        <stop offset="0" stop-color="#6f7b8c"/>
        <stop offset="1" stop-color="#5d6a7c"/>
      </radialGradient>
    </defs>
    <circle cx="500.6" cy="91.3" r="310.4" fill="url(#frontGlow)"/>
  </svg>
  <div class="abs" role="img" aria-label="Soft faded background photo of a patient care scene" style="left:330px;top:0;width:277px;height:190px;background:linear-gradient(200deg,rgba(255,255,255,.10),rgba(255,255,255,0) 70%);"></div>

  <div class="abs brand" style="left:29px;top:55px;">
    <span class="brand__dot"></span>
    <span class="brand__name">Harborline<br>Family Clinic</span>
  </div>

  <h1 class="abs headline"><span>REFER YOUR</span><span class="second">FAMILY &amp; FRIENDS</span></h1>
  <div class="abs tagline-pill">YOUR HEALTH, YOUR TIME, YOUR WAY</div>
  <p class="abs subline">PERSONALIZED CARE MEETS MODERN MEDICINE</p>

  <div class="abs" role="img" aria-label="Portrait photo of Dr. Malvina Okoruwe, MD, smiling, in a dark blue jacket"
       style="left:350px;top:191px;width:197px;height:232px;border-radius:90px 90px 0 0;background:linear-gradient(180deg,#3a3f4c 0%,#2a2f3e 55%,#1c2238 100%);"></div>

  <h2 class="abs doctor-name">DR. MALVINA OKORUWE, MD</h2>
  <p class="abs doctor-bio">Dr. Malvina Okoruwe joined<br>Harborline Family Clinic in July<br>2024. She is Board certified,<br>bilingual (English/ Spanish)<br>Family Physician with 27 years<br>of diverse clinical experience.</p>

  <p class="abs cta-kicker">CALL/EMAIL TO SCHEDULE</p>
  <p class="abs cta-main">FREE CONSULTATION</p>
  <div class="abs phone-pill phone-pill--slate">
    <span class="phone-pill__icon">
      <svg width="14" height="14" viewBox="0 0 24 24"><path fill="#5d6a7c" d="M6.6 10.8a15.1 15.1 0 0 0 6.6 6.6l2.2-2.2c.3-.3.7-.4 1-.2 1.1.4 2.3.6 3.6.6.6 0 1 .4 1 1V20c0 .6-.4 1-1 1A17 17 0 0 1 3 4c0-.6.4-1 1-1h3.5c.6 0 1 .4 1 1 0 1.2.2 2.4.6 3.6.1.3 0 .7-.2 1z"/></svg>
    </span>(727) 482-3095
  </div>
  <p class="abs contact-line" style="top:365px;">
    <svg viewBox="0 0 24 24"><path fill="#4f5b6b" d="M2 5h20v14H2zm2 2v.5l8 5 8-5V7z"/></svg>office@harborlinefamilyclinic.org</p>
  <p class="abs contact-line" style="top:382px;">
    <svg viewBox="0 0 24 24"><circle cx="12" cy="12" r="10" fill="#4f5b6b"/><path fill="#fff" d="M8 6c2 1 3 3 2 5-1 1-3 1-3 3s2 3 1 5c-3-1-5-4-5-7 0-3 2-5 5-6zm7 1c2 1 3 3 1 4-1 1 0 3 2 3 0 2-1 4-3 4 0-2-2-2-2-4s2-2 2-4c-1-1-1-2 0-3z"/></svg>www.harborlinefamilyclinic.org</p>
</section>

<p class="side-label" style="top:575px;">FRONT SIDE</p>

<!-- BACK -->
<section class="postcard postcard--back">
  <div class="abs" role="img" aria-label="Black and white photo of a smiling physician talking with a patient in an exam room"
       style="left:0;top:0;width:230px;height:175px;background:linear-gradient(180deg,#8e949c 0%,#7d8590 60%,#5d6a7c 100%);"></div>
  <svg class="shapes" viewBox="0 0 607 423" width="607" height="423" aria-hidden="true">
    <circle cx="506" cy="105.4" r="299" fill="#ffffff"/>
  </svg>

  <div class="abs brand" style="left:236px;top:48px;">
    <span class="brand__dot"></span>
    <span class="brand__name">Harborline<br>Family Clinic</span>
  </div>

  <p class="abs return-address"><strong>Harborline Family Clinic</strong><br>4187 Wrenfield Ave<br>Suite 214<br>Clearwater, FL 33759</p>
  <div class="abs indicia">PRSRT STD<br>ECRWSS<br>U.S. POSTAGE<br>PAID<br>EDDM RETAIL</div>

  <h2 class="abs benefits-title">BENEFITS OF CONCIERGE MEDICINE<br>WITH HARBORLINE FAMILY CLINIC</h2>
  <ul class="abs benefits-list">
    <li>The finest internal &amp; functional medical care</li>
    <li>24/7 access to our team via email, phone, &amp; text</li>
    <li>Same or next-day appointments</li>
    <li>Accompaniment by our team to specialist visits if necessary</li>
    <li>Advocacy during hospitalization</li>
    <li>In-office or at-home blood draws</li>
    <li>Proactive vs. reactive medical care</li>
    <li>Travel assistance</li>
    <li>Comprehensive annual physical exam</li>
    <li>Gynecological care</li>
    <li>And more</li>
  </ul>

  <div class="abs mail-block">Local<br>Postal Customer</div>

  <h2 class="abs welcome">WELCOMING NEW<br>PATIENTS NOW!</h2>
  <p class="abs welcome-copy">We welcome new patients, but because of our exclusivity, we ask prospective patients to submit online request to see if we have openings for an initial visit.</p>

  <p class="abs cta-kicker">CALL/EMAIL TO SCHEDULE</p>
  <p class="abs cta-main">FREE CONSULTATION</p>
  <div class="abs phone-pill phone-pill--white">
    <span class="phone-pill__icon">
      <svg width="13" height="13" viewBox="0 0 24 24"><path fill="#ffffff" d="M6.6 10.8a15.1 15.1 0 0 0 6.6 6.6l2.2-2.2c.3-.3.7-.4 1-.2 1.1.4 2.3.6 3.6.6.6 0 1 .4 1 1V20c0 .6-.4 1-1 1A17 17 0 0 1 3 4c0-.6.4-1 1-1h3.5c.6 0 1 .4 1 1 0 1.2.2 2.4.6 3.6.1.3 0 .7-.2 1z"/></svg>
    </span>(727) 482-3095
  </div>
  <p class="abs contact-line" style="top:364px;">
    <svg viewBox="0 0 24 24"><path fill="#ffffff" d="M2 5h20v14H2zm2 2v.5l8 5 8-5V7z"/></svg>office@harborlinefamilyclinic.org</p>
  <p class="abs contact-line" style="top:382px;">
    <svg viewBox="0 0 24 24"><circle cx="12" cy="12" r="10" fill="#ffffff"/><path fill="#5d6a7c" d="M8 6c2 1 3 3 2 5-1 1-3 1-3 3s2 3 1 5c-3-1-5-4-5-7 0-3 2-5 5-6zm7 1c2 1 3 3 1 4-1 1 0 3 2 3 0 2-1 4-3 4 0-2-2-2-2-4s2-2 2-4c-1-1-1-2 0-3z"/></svg>www.harborlinefamilyclinic.org</p>
</section>

<p class="side-label" style="top:1085px;">BACK SIDE</p>

</body>
</html>
```